Flyer Design for a Boston Therapeutic Clinic

I am a body therapist who needs a couple of flyers designed:
1. To fit half a page.
2. To fit a 5 inch by 3.5 inch flyer.
My practice is based in Boston, MA and my web site is:
www.LarkfieldTane.Com
For the First half page:
A. Have my company's name and color shown as it appears on my web site (Larkfield Tane)
B. Have the following text: "Control your weight (This part should be emphasized) by balancing your nervous and digestive system through the Tane Method. The Tane Method, a technique developed by Dr. Wenna. Tane, uses physical pressure to manipulate visceral tissue to bring back resiliency and proper functioning of the whole body."
Also helps with
-Constipation
-Bloating
-IBS
-eating disorders and overeating
Our practitioner is highly experienced. Please visit our web sites for reviews.
C. I would like to have a nice earthy feeling, something that feels "freeing" like open flowers, or an open land scape such as mountains or fields.
D. I also like the color blue, white, orange; perhaps if these colors can be integrated into the flyer, that would be great.
E. "Visit our web site LarkfieldTane.com or call 413-908-2617"
The Smaller Flyer :
A.The smaller Flyer should also have my Company's name as shown on my web site (Larkfield Tane)
B.The following text: " Restore your body's natural resiliency and greatly reduce your physical pain through the Dr. Wenna Tane Method of Structural Integration."
C. "Our practitioner is highly experienced and has a great reputation; visit our web site for reviews."
"Benefits:
"reduce aches and pains
reduce joint pain
reduce chronic muscular tension"
D, "feel better after the first session!"
E. if you could use a picture of me working on someone from my web site, that would be great.
F. I also like the colors white, orange and silver, for this one.
G. "Visit our web site LarkfieldTane.com or call 413-908 2617"
I am very open minded,
I would like the flyer to evoke a sense of tranquility, professionalism, and simplicity. So if you have another angle you think would look good, then go for it! As long as it looks clean, professional and helpful.
Thanks a lot!
If you need any pictures from my web site, I have the original high resolution files that i can send.
Professionals and working men and women from ages 20-70
Clinic

```html
<!DOCTYPE html>
<html lang="en">
<head>
<meta charset="utf-8">
<title>Larkfield Tane Therapy – Flyer</title>
<link rel="stylesheet" href="https://fonts.googleapis.com/css2?family=Cutive&family=Courier+Prime:wght@700&display=swap">
<style>
  :root {
    --paper: #f2f5c9;
    --leaf-dark: #3f7a23;
    --leaf-mid: #7fb83a;
    --leaf-light: #c9e39a;
    --brand-red: #e8432a;
    --slate: #56667a;
    --body-ink: #4e5a6a;
    --accent-blue: #1d2fd4;
    --list-blue: #2636c2;
    --badge: #ec4b1e;
    --white: #ffffff;
  }
  * { margin: 0; padding: 0; box-sizing: border-box; }
  html, body { width: 1200px; height: 856px; overflow: hidden; background: var(--paper); }
  .flyer {
    position: relative;
    width: 1200px;
    height: 856px;
    background: var(--paper);
    font-family: "Cutive", "Courier New", serif;
    overflow: hidden;
  }
  .hero-photo {
    position: absolute;
    left: 0; top: 0;
    width: 640px; height: 856px;
    background:
      linear-gradient(to right, rgba(242,245,201,0) 0%, rgba(242,245,201,0) 72%, var(--paper) 100%),
      radial-gradient(ellipse at 45% 30%, var(--leaf-light) 0%, var(--leaf-mid) 45%, var(--leaf-dark) 100%);
  }
  .brand {
    position: absolute;
    left: 440px; top: 34px;
    width: 740px;
    text-align: right;
    font-size: 51px;
    line-height: 60px;
    font-weight: 400;
    white-space: nowrap;
  }
  .brand-name { color: var(--brand-red); }
  .brand-rest { color: var(--slate); }
  .intro {
    position: absolute;
    left: 590px; top: 110px;
    width: 600px;
    font-size: 25px;
    line-height: 37.5px;
    color: var(--body-ink);
    white-space: nowrap;
  }
  .intro strong {
    font-family: "Courier Prime", "Courier New", monospace;
    font-weight: 700;
    font-size: 26px;
    line-height: 37.5px;
    color: var(--accent-blue);
  }
  .benefits {
    position: absolute;
    left: 602px; top: 434px;
    font-size: 23px;
    line-height: 35.5px;
    color: var(--list-blue);
    list-style: none;
    white-space: nowrap;
  }
  .benefits li.indent { padding-left: 7px; }
  .badge {
    position: absolute;
    left: 915px; top: 398px;
    width: 261px; height: 261px;
    border-radius: 50%;
    background: var(--badge);
    color: var(--white);
    text-align: center;
    padding-top: 22px;
  }
  .badge-claim {
    font-family: "Courier Prime", "Courier New", monospace;
    font-weight: 700;
    font-size: 22px;
    line-height: 28px;
  }
  .badge-note {
    font-size: 19px;
    line-height: 28px;
  }
  .contact {
    position: absolute;
    left: 580px; top: 682px;
    width: 600px;
    text-align: center;
    font-size: 40px;
    line-height: 56px;
    color: var(--slate);
    white-space: nowrap;
  }
</style>
</head>
<body>
<div class="flyer">
  <div class="hero-photo" role="img" aria-label="Woman seen from behind with arms raised in a lush green tropical forest"></div>

  <h1 class="brand"><span class="brand-name">Larkfield</span> <span class="brand-rest">Tane Therapy</span></h1>

  <p class="intro"><strong>Control your weight</strong> by balancing<br>your nervous and digestive system<br>through the Tane Method. The Tane<br>Method, a technique developed by Dr.<br>Wenna. Tane, uses physical pressure to<br>manipulate visceral tissue to bring<br>back resiliency and proper functioning<br>of the whole body.</p>

  <ul class="benefits">
    <li>Also helps with</li>
    <li>-Constipation</li>
    <li>-Bloating</li>
    <li>-IBS</li>
    <li>-eating disorders and</li>
    <li class="indent">overeating</li>
  </ul>

  <div class="badge">
    <p class="badge-claim">Our<br>practitioner<br>is highly<br>experienced.</p>
    <p class="badge-note">Please visit our<br>web sites for<br>reviews.</p>
  </div>

  <div class="contact">
    <p>Visit our website</p>
    <p>www.LarkfieldTane.com</p>
    <p>or call 413-908-2617</p>
  </div>
</div>
</body>
</html>
```